Wedding Invitations

We are a printing company "inkmakers" and require multiple wedding invitation designs for our customers in store and online. We would like the designs to be editable in Photoshop if possible, if not then a layout with suggested fonts would be the next best option. We are open to suggestions on design but would like to stick to the general wedding themes some with a modern and some with a classical feel

Industry/Entity Type

Printing

```html
<!DOCTYPE html>
<html lang="en">
<head>
<meta charset="utf-8">
<title>Wedding Invitation Suite</title>
<link href="https://fonts.googleapis.com/css2?family=Great+Vibes&family=Lobster&display=swap" rel="stylesheet">
<style>
  :root {
    --backdrop: #ecebe8;
    --crimson-dark: #7e1717;
    --crimson-stripe: #8e2020;
    --ribbon-red: #e3262b;
    --badge-maroon: #5c1014;
    --frame-white: #ffffff;
    --crimson-text: #a3322a;
    --blush-paper: #fbf4f7;
    --tree-lilac: #d8cde2;
    --tree-pink: #e9a8c6;
    --heart-pink: #f39bbb;
    --plum-text: #5f2460;
    --magenta-text: #a1178b;
    --ivory-paper: #ffffff;
    --damask-cream: #ede5d0;
    --damask-gold: #d8ccaa;
    --taupe-band: #d3c9aa;
    --sepia-text: #6a624c;
    --frame-taupe: #9d9272;
  }
  * { box-sizing: border-box; margin: 0; padding: 0; }
  html, body { width: 1200px; height: 849px; overflow: hidden; background: var(--backdrop); }
  .suite { position: relative; width: 1200px; height: 849px; }

  .card { position: absolute; width: 460px; height: 330px; box-shadow: 0 6px 14px rgba(0,0,0,.22); overflow: hidden; }

  /* Classic crimson card */
  .card--crimson { left: 70px; top: 100px; background: repeating-linear-gradient(90deg, var(--crimson-dark) 0 6px, var(--crimson-stripe) 6px 9px); }
  .card--crimson svg { position: absolute; inset: 0; }
  .crimson-text { position: absolute; left: 60px; top: 122px; width: 360px; text-align: center; font-family: "Lobster", cursive; color: var(--crimson-text); font-size: 21px; line-height: 29px; }
  .crimson-text .couple { font-size: 25px; line-height: 33px; }

  /* Modern blossom card */
  .card--blossom { left: 390px; top: 250px; background: var(--blush-paper); }
  .blossom-tree { position: absolute; left: 25px; top: 95px; width: 160px; height: 160px; border-radius: 50%;
    background: radial-gradient(circle at 45% 40%, var(--tree-pink) 0 35%, var(--tree-lilac) 70%); }
  .blossom-heart { position: absolute; left: 282px; top: 52px; }
  .blossom-text { position: absolute; left: 205px; top: 110px; width: 250px; text-align: center; font-family: "Lobster", cursive; color: var(--plum-text); font-size: 17px; line-height: 22px; }
  .blossom-text .name { color: var(--magenta-text); font-size: 23px; line-height: 30px; }

  /* Classic damask card */
  .card--damask { left: 690px; top: 400px; width: 470px; background: var(--ivory-paper); }
  .damask-field { position: absolute; left: 0; top: 0; width: 100%; height: 250px;
    background: linear-gradient(135deg, var(--damask-cream), var(--damask-gold) 60%, var(--damask-cream)); }
  .taupe-band { position: absolute; left: 0; top: 250px; width: 100%; height: 80px; background: var(--taupe-band); }
  .monogram-box { position: absolute; left: 28px; top: 228px; width: 84px; height: 84px; background: var(--ivory-paper);
    border: 1px solid var(--frame-taupe); outline: 3px solid var(--ivory-paper); font-family: "Great Vibes", cursive;
    color: var(--sepia-text); font-size: 34px; line-height: 36px; padding: 6px 0 0 12px; }
  .monogram-box span { display: block; }
  .monogram-box span:last-child { padding-left: 26px; }
  .verse-panel { position: absolute; left: 245px; top: 22px; width: 200px; height: 284px; background: var(--ivory-paper);
    border: 1px solid var(--frame-taupe); outline: 4px solid var(--ivory-paper); text-align: center;
    font-family: "Great Vibes", cursive; color: var(--sepia-text); font-size: 12px; line-height: 14.5px; padding: 18px 10px; }
  .verse-panel .name { font-size: 17px; line-height: 22px; }
</style>
</head>
<body>
<main class="suite">

  <article class="card card--crimson">
    <svg width="460" height="330" viewBox="0 0 460 330">
      <path d="M70,40 H390 A30,30 0 0 0 420,70 V275 A30,30 0 0 0 390,305 H70 A30,30 0 0 0 40,275 V70 A30,30 0 0 0 70,40 Z" fill="var(--frame-white)"/>
      <path d="M76,48 H384 A28,28 0 0 0 412,76 V269 A28,28 0 0 0 384,297 H76 A28,28 0 0 0 48,269 V76 A28,28 0 0 0 76,48 Z" fill="none" stroke="var(--crimson-text)" stroke-width="1"/>
      <rect x="0" y="62" width="460" height="36" fill="var(--ribbon-red)"/>
      <line x1="0" y1="69" x2="460" y2="69" stroke="var(--frame-white)" stroke-width="2"/>
      <line x1="0" y1="91" x2="460" y2="91" stroke="var(--frame-white)" stroke-width="2"/>
      <ellipse cx="190" cy="80" rx="50" ry="38" fill="var(--badge-maroon)" stroke="var(--frame-white)" stroke-width="3"/>
      <text x="190" y="91" text-anchor="middle" font-family="Great Vibes, cursive" font-size="30" fill="var(--frame-white)">L&amp;O</text>
    </svg>
    <div class="crimson-text">
      <p>The honor of your presence is requested</p>
      <p>at the marriage of</p>
      <p class="couple">Lena Marie Hart</p>
      <p class="couple">to Owen Thomas Brooks</p>
      <p>Saturday, the twelfth of October</p>
    </div>
  </article>

  <article class="card card--blossom">
    <div class="blossom-tree" role="img" aria-label="Illustration of a tree with a round crown of pink and lilac heart blossoms"></div>
    <svg class="blossom-heart" width="42" height="38" viewBox="0 0 42 38" aria-hidden="true">
      <path d="M21,36 C8,26 1,18 1,11 C1,5 6,1 11,1 C15,1 19,3 21,8 C23,3 27,1 31,1 C36,1 41,5 41,11 C41,18 34,26 21,36 Z" fill="var(--heart-pink)"/>
    </svg>
    <div class="blossom-text">
      <p>Together with their parents</p>
      <p class="name">Clara Isabel Vanmoren</p>
      <p>and</p>
      <p class="name">Daniel Kristian Pollard</p>
      <p>request the honour of your presence</p>
      <p>at their marriage</p>
      <p>on Sunday, the ninth of June</p>
    </div>
  </article>

  <article class="card card--damask">
    <div class="damask-field" role="img" aria-label="Repeating gold damask ornament pattern"></div>
    <div class="taupe-band"></div>
    <div class="monogram-box"><span>M</span><span>&amp;J</span></div>
    <div class="verse-panel">
      <p>Because you have shared in</p>
      <p>our lives by your friendship and love, we</p>
      <p class="name">Maren Elise Whitford</p>
      <p>and</p>
      <p class="name">Jonah Edward Lindqvist</p>
      <p>together with our parents</p>
      <p>invite you to share</p>
      <p>the beginning of our new life together</p>
      <p>when we exchange marriage vows</p>
      <p>on Friday, the eleventh of May</p>
      <p>two thousand eighteen at half after four o'clock</p>
      <p>The Hall of Villa Serena</p>
      <p>Twelve Harbor Lane</p>
      <p>Port Alder, Florida</p>
    </div>
  </article>

</main>
</body>
</html>
```